Business Cards, Letterheads, Envelopes

A company's new identity to be reflected on its stationery items

Target Market(s)

Large Corporate Companies & Enterprises

Font styles to use
Sans Serif

Colors
0555a3
3176b5
85abd2
85cae6
33a6d7
0293ce

```html
<!DOCTYPE html>
<html lang="en">
<head>
<meta charset="utf-8">
<title>Corvane Nexus — Stationery Set</title>
<link rel="stylesheet" href="https://fonts.googleapis.com/css2?family=Michroma&display=swap">
<style>
  :root {
    --navy-bg: #1a3052;
    --brand-deep: #0555a3;
    --brand-mid: #3176b5;
    --brand-soft: #85abd2;
    --brand-sky: #85cae6;
    --brand-cyan: #0293ce;
    --paper: #ffffff;
    --card-paper: #f4f4f4;
  }
  html, body {
    margin: 0;
    padding: 0;
    width: 1200px;
    height: 1200px;
    overflow: hidden;
    background: var(--navy-bg);
  }
  .stationery-board {
    position: relative;
    width: 1200px;
    height: 1200px;
  }
  .item {
    position: absolute;
    display: block;
    filter: drop-shadow(0 18px 14px rgba(5, 15, 30, 0.55));
  }
  .letterhead { left: 62px; top: 43px; width: 508px; height: 728px; }
  .folder { left: 627px; top: 40px; width: 510px; height: 730px; }
  .card-front { left: 61px; top: 829px; width: 508px; height: 290px; }
  .card-back { left: 628px; top: 829px; width: 508px; height: 291px; }
  .brand-name {
    font-family: "Michroma", "Arial", sans-serif;
    fill: var(--brand-mid);
  }
  .brand-dot { fill: var(--brand-mid); }
  .icon-disc { fill: var(--brand-deep); }
  .icon-glyph { fill: none; stroke: #ffffff; stroke-width: 2.4; stroke-linecap: round; stroke-linejoin: round; }
  .icon-fill { fill: #ffffff; }
</style>
</head>
<body>
<svg width="0" height="0" style="position:absolute" aria-hidden="true">
  <defs>
    <g id="brand-name-mark">
      <circle class="brand-dot" cx="0" cy="0" r="34"/>
      <text class="brand-name" x="56" y="10" font-size="28" textLength="290" lengthAdjust="spacingAndGlyphs">CORVANE NEXUS</text>
    </g>
    <g id="icon-phone">
      <circle class="icon-disc" r="17"/>
      <path class="icon-fill" d="M-7,-9 L-3,-9 L-1,-4 L-4,-2 Q-1,4 3,5 L5,2 L10,4 L10,8 Q9,10 6,10 Q-8,7 -10,-6 Q-10,-9 -7,-9 Z"/>
    </g>
    <g id="icon-globe">
      <circle class="icon-disc" r="17"/>
      <circle class="icon-glyph" r="10"/>
      <ellipse class="icon-glyph" rx="4.5" ry="10"/>
      <line class="icon-glyph" x1="-10" y1="0" x2="10" y2="0"/>
    </g>
    <g id="icon-mail">
      <circle class="icon-disc" r="17"/>
      <rect class="icon-glyph" x="-9" y="-6" width="18" height="12" rx="1"/>
      <polyline class="icon-glyph" points="-9,-6 0,2 9,-6"/>
    </g>
    <g id="icon-pin">
      <circle class="icon-disc" r="17"/>
      <path class="icon-fill" d="M0,11 Q-8,1 -8,-3 A8,8 0 1 1 8,-3 Q8,1 0,11 Z"/>
      <circle class="icon-disc" cx="0" cy="-3" r="3"/>
    </g>
  </defs>
</svg>

<main class="stationery-board">
  <!-- Letterhead -->
  <svg class="item letterhead" viewBox="0 0 818 1171" preserveAspectRatio="none">
    <rect width="818" height="1171" fill="var(--paper)"/>
    <rect class="network-decor" x="0" y="0" width="170" height="240" fill="var(--brand-sky)" opacity="0.35" role="img" aria-label="Connected-node network decoration, top left corner"/>
    <rect class="network-decor" x="620" y="0" width="198" height="120" fill="var(--brand-sky)" opacity="0.35" role="img" aria-label="Connected-node network decoration, top right corner"/>
    <line x1="0" y1="285" x2="818" y2="142" stroke="var(--brand-sky)" stroke-width="9"/>
    <use href="#brand-name-mark" transform="translate(226,124)"/>
    <polygon points="0,959 818,816 818,1171 0,1171" fill="var(--brand-sky)"/>
    <polygon points="0,960 572,1090 818,1147 818,1171 0,1171" fill="var(--brand-deep)"/>
    <polygon points="572,1090 818,1035 818,1147" fill="var(--brand-cyan)"/>
  </svg>

  <!-- Folder / cover -->
  <svg class="item folder" viewBox="0 0 821 1175" preserveAspectRatio="none">
    <rect width="821" height="1175" fill="var(--paper)"/>
    <polygon points="0,0 821,0 821,25 572,82 0,212" fill="var(--brand-deep)"/>
    <polygon points="0,212 572,82 821,137 821,355" fill="var(--brand-sky)"/>
    <polygon points="572,82 821,25 821,137" fill="var(--brand-cyan)"/>
    <use href="#brand-name-mark" transform="translate(255,530)"/>
    <polygon points="0,963 821,819 821,1175 0,1175" fill="var(--brand-sky)"/>
    <polygon points="0,963 572,1093 821,1150 821,1175 0,1175" fill="var(--brand-deep)"/>
    <polygon points="572,1093 821,1038 821,1150" fill="var(--brand-cyan)"/>
  </svg>

  <!-- Business card, front -->
  <svg class="item card-front" viewBox="0 0 818 467" preserveAspectRatio="none">
    <rect width="818" height="467" fill="var(--card-paper)"/>
    <rect y="402" width="818" height="65" fill="var(--paper)"/>
    <line x1="0" y1="403" x2="818" y2="403" stroke="var(--brand-deep)" stroke-width="3"/>
    <use href="#brand-name-mark" transform="translate(236,194)"/>
    <use href="#icon-phone" transform="translate(38,437)"/>
    <use href="#icon-globe" transform="translate(192,437)"/>
    <use href="#icon-mail" transform="translate(364,437)"/>
    <use href="#icon-pin" transform="translate(570,437)"/>
  </svg>

  <!-- Business card, back -->
  <svg class="item card-back" viewBox="0 0 818 468" preserveAspectRatio="none">
    <rect width="818" height="468" fill="var(--card-paper)"/>
    <path d="M315,0 Q700,30 818,200 L818,0 Z" fill="var(--brand-sky)"/>
    <path d="M315,0 L818,0 L818,148 Q620,10 315,0 Z" fill="var(--brand-deep)"/>
    <path d="M0,270 Q150,430 500,468 L0,468 Z" fill="var(--brand-sky)"/>
    <path d="M0,320 Q180,440 500,468 L0,468 Z" fill="var(--brand-deep)"/>
    <use href="#brand-name-mark" transform="translate(120,165) scale(0.7)"/>
    <line x1="409" y1="125" x2="409" y2="400" stroke="var(--brand-deep)" stroke-width="2"/>
    <use href="#icon-phone" transform="translate(478,158)"/>
    <use href="#icon-globe" transform="translate(478,227)"/>
    <use href="#icon-mail" transform="translate(478,296)"/>
    <use href="#icon-pin" transform="translate(478,364)"/>
  </svg>
</main>
</body>
</html>
```